Business card design needed

Velvet Moxie is an online boutique for connoisseurs of unique, hand crafted, vintage and pin-up inspired lingerie, delectable handmade lotions & potions and naughty & nice, seduce me please gifts and ideas.

Inspired by vintage glamour, pin-up and burlesque, the site is dedicated to things that make all women look and feel beautiful…with a touch of mischief.

The design should be clean, uncomplicated, sophisticated and in line with the website - See www.velvetmoxie.com.au.

Predominantly black, red and grey in colour.

Font used on the website is Honeyscript and Drescher Grotesk Light

Industry/Entity Type

Boutique

Contact Information for Business Card

Velvet Moxie
Corinne Walsby - Director
0417 639 204
corinne@velvetmoxie.com.au

Requirements
Should not have
• No lace, nothing to girly.

```html
<!DOCTYPE html>
<html lang="en">
<head>
<meta charset="utf-8">
<title>Velvet Moxie – Business Card</title>
<link rel="stylesheet" href="https://fonts.googleapis.com/css2?family=Questrial&display=swap">
<style>
  :root {
    --stage: #2a2a2c;
    --card-black: #0d0d0e;
    --card-black-tone: #1b1b1d;
    --card-grey: #dcdcdc;
    --card-grey-tone: #cfcfcf;
    --brand-red: #9b2a1c;
    --ink: #1a1a1a;
  }
  * { margin: 0; padding: 0; box-sizing: border-box; }
  html, body {
    width: 1200px; height: 900px; overflow: hidden;
    background: var(--stage);
    font-family: "Questrial", "Century Gothic", sans-serif;
  }
  .sheet {
    position: relative; width: 1200px; height: 900px;
  }
  .card {
    position: absolute; left: 320px; width: 560px; height: 320px;
    overflow: hidden;
    box-shadow: 0 10px 30px rgba(0,0,0,.45);
  }
  .card--front { top: 110px; }
  .card--back  { top: 470px; }

  .card__ground { position: absolute; inset: 0; }
  .card--front .card__ground {
    background: radial-gradient(ellipse at 50% 45%, var(--card-black-tone), var(--card-black) 75%);
  }
  .card--back .card__ground {
    background: radial-gradient(ellipse at 50% 50%, var(--card-grey), var(--card-grey-tone) 85%);
  }

  /* front */
  .brand {
    position: absolute; left: 58px; right: 40px; top: 148px;
    display: flex; align-items: center; gap: 14px;
  }
  .brand__mark {
    width: 14px; height: 14px; border-radius: 50%;
    background: var(--brand-red); flex: none;
  }
  .brand__name {
    color: var(--brand-red); font-size: 40px; letter-spacing: 7px;
    text-transform: uppercase; white-space: nowrap;
  }
  .brand__rule {
    position: absolute; left: 58px; right: 40px; top: 232px;
    height: 1px; background: var(--brand-red);
  }
  .brand__web {
    position: absolute; right: 40px; top: 212px;
    color: var(--brand-red); font-size: 11px; letter-spacing: 2px;
  }

  /* back */
  .offer-list {
    position: absolute; left: 62px; top: 102px;
    list-style: none; color: var(--ink); font-size: 19px; line-height: 40px;
  }
  .offer-list li::before {
    content: "- "; color: var(--brand-red);
  }
</style>
</head>
<body>
<main class="sheet">
  <section class="card card--front" aria-label="Card front">
    <div class="card__ground" role="img" aria-label="Black card with a faint tone-on-tone damask pattern"></div>
    <div class="brand">
      <span class="brand__mark"></span>
      <span class="brand__name">Velvet Moxie</span>
    </div>
    <p class="brand__web">www.velvetmoxie.com.au</p>
    <div class="brand__rule"></div>
  </section>

  <section class="card card--back" aria-label="Card back">
    <div class="card__ground" role="img" aria-label="Light grey card with a faint tone-on-tone damask pattern"></div>
    <ul class="offer-list">
      <li>Hand crafted, vintage and pin-up inspired lingerie</li>
      <li>Delectable, handmade lotions &amp; potions</li>
      <li>Naughty &amp; nice, seduce me please gifts and ideas</li>
    </ul>
  </section>
</main>
</body>
</html>
```